Mini Book (4.25 x 6) Cover Design for Christian authors

We need a book cover designed for a mini book (4.25 x 6). We will need a front, back and spine for the book.
The book is titled:
Harbor Lanterns
Subtitle:
Hidden Meaning in Your Name
Authors:
Walter and Renata Oskarsby
We are wanting the colors Dark Blue and Grey with more blue than grey.
We do not want any stock images or photos, only original work.
The cover should convey sincerity, intuition and truth with prestige.
We want the back cover text to be included (top) and the bios to be on the back as well (bottom). *Those documents are included in the files.
Since it is a mini book, it is important for the design to be simple and not cluttered, but powerful!
This is the first book in a twelve book series, so we would like the same "look" to carry through all twelve books, eventually.
On the back of the book, at the bottom (left), we want the following contact information:
Bright Meadow Method Logo (in files below)
tallwillowstudio@mailfernly.com
303.512.4086
P.O.Box 718
Pinecrest, CO 80417

Please save room on the back (bottom-right) for the ISBN and price.
Updates

Thank you to the designers that have submitted feedback concerning our design brief. We have made some changes that will perhaps make it easier to submit a variety of designs.Thank you! Added Saturday, March 4, 2017

Target Market(s)

Christians - mainly women

Industry/Entity Type

Religious

Font styles to use
Serif
Sans Serif
Decorative
Script
Other font styles liked:
• Not any particular font, looking for one that goes well with the cover design.

Requirements
Must have
• Mini Book Size (4.25 x 6)-spine size 1/8" (0.125)
• Dark blue and grey colors
• Cover needs to be simple and not cluttered or busy.
• Intriguing
• A font that is attractive, but it is still easy to read.
• *File information below
Nice to have
• Designs that are different from the mainstream.
• Perhaps a design that would do something different with the title/font? Maybe a repeat of the words from smaller to larger? Not sure how it would look, but maybe?
Should not have
• Any other colors but dark blue and grey
• Cluttered Look

```html
<!DOCTYPE html>
<html lang="en">
<head>
<meta charset="utf-8">
<title>Harbor Lanterns – Cover Spread</title>
<link href="https://fonts.googleapis.com/css2?family=Roboto+Condensed:wght@700&family=PT+Sans+Narrow:wght@400;700&family=PT+Sans:ital,wght@0,400;1,400&family=Cinzel:wght@400&display=swap" rel="stylesheet">
<style>
  :root {
    --page: #efebe6;
    --navy: #0b3566;
    --sky: #8fd3e8;
    --white: #ffffff;
    --silver: #c9ccd1;
    --ink-dark: #0d2b4d;
    --rule: #3d5f8a;
  }
  * { margin: 0; padding: 0; box-sizing: border-box; }
  html, body { width: 1200px; height: 1200px; overflow: hidden; background: var(--page); }

  .spread {
    position: absolute;
    left: 22.5px; top: 215px;
    width: 1050px; height: 700px;
    transform: scale(1.1);
    transform-origin: top left;
    background: var(--navy);
    color: var(--white);
    font-family: "PT Sans", sans-serif;
  }

  .title-metal {
    font-family: "Roboto Condensed", sans-serif;
    font-weight: 700;
    background: linear-gradient(180deg, var(--white) 0%, var(--white) 45%, var(--silver) 100%);
    -webkit-background-clip: text;
    background-clip: text;
    color: transparent;
    letter-spacing: -1px;
  }

  /* Back cover */
  .back { position: absolute; left: 0; top: 0; width: 495px; height: 700px; }
  .back-title { position: absolute; left: 40px; top: 26px; width: 428px; text-align: center; font-size: 66px; line-height: 1.15; letter-spacing: -1.5px; }
  .back-subtitle { position: absolute; left: 47px; top: 114px; width: 414px; text-align: center; font-family: "PT Sans Narrow", sans-serif; font-size: 30px; line-height: 36px; color: var(--sky); }

  .method-mark { position: absolute; left: 52px; top: 172px; width: 100px; text-align: center; }
  .method-mark .dot { width: 62px; height: 62px; margin: 0 auto 6px; border-radius: 50%; background: var(--sky); }
  .method-mark .name { font-family: "PT Sans Narrow", sans-serif; font-size: 13px; line-height: 1.2; color: var(--white); }

  .blurb { position: absolute; left: 171px; top: 166px; width: 288px; font-family: "PT Sans Narrow", sans-serif; font-size: 13.5px; line-height: 17.5px; text-align: justify; }
  .promise { position: absolute; left: 171px; top: 268px; width: 288px; font-family: "PT Sans Narrow", sans-serif; font-size: 13.5px; line-height: 17.5px; }
  .promise ul { list-style: none; margin-top: 1px; }
  .promise li { padding-left: 14px; position: relative; }
  .promise li::before { content: "•"; position: absolute; left: 2px; }

  .bio { position: absolute; left: 48px; top: 356px; width: 411px; font-family: "PT Sans Narrow", sans-serif; font-size: 13.5px; line-height: 17.5px; text-align: justify; }

  .verse { position: absolute; left: 46px; top: 459px; width: 412px; height: 80px; background: var(--sky); border-radius: 6px; color: var(--ink-dark); font-style: italic; font-size: 12.5px; line-height: 17.5px; padding: 12px 24px; text-align: justify; }

  .contact { position: absolute; left: 49px; top: 563px; font-family: "PT Sans Narrow", sans-serif; font-size: 13.5px; line-height: 17.5px; }
  .contact p { margin-bottom: 9px; }
  .contact p.addr { margin-bottom: 0; }
  .isbn-space { position: absolute; left: 279px; top: 563px; width: 179px; height: 107px; background: var(--white); }

  /* Spine */
  .spine { position: absolute; left: 495px; top: 0; width: 60px; height: 700px; border-left: 1px solid var(--rule); border-right: 1px solid var(--rule); }
  .spine-run { position: absolute; left: 60px; top: 30px; width: 650px; height: 60px; transform: rotate(90deg); transform-origin: top left; display: flex; align-items: center; gap: 18px; }
  .spine-title { font-size: 44px; line-height: 1; white-space: nowrap; }
  .spine-sub { font-family: "PT Sans Narrow", sans-serif; font-size: 21px; line-height: 19px; color: var(--sky); white-space: nowrap; }
  .spine-authors { font-family: "Cinzel", serif; font-size: 14px; line-height: 15px; white-space: nowrap; margin-left: 8px; }

  /* Front cover */
  .front { position: absolute; left: 555px; top: 0; width: 495px; height: 700px; text-align: center; }
  .front-title { position: absolute; left: 0; top: 30px; width: 495px; line-height: 0.98; }
  .front-title .line-one { display: block; font-size: 138px; }
  .front-title .line-two { display: block; font-size: 112px; }
  .front-subtitle { position: absolute; left: 0; top: 400px; width: 495px; font-family: "PT Sans Narrow", sans-serif; font-weight: 700; font-size: 46px; line-height: 58px; color: var(--sky); letter-spacing: -0.5px; }
  .front-authors { position: absolute; left: 0; top: 576px; width: 495px; font-family: "Cinzel", serif; font-size: 31px; line-height: 37px; }
</style>
</head>
<body>
  <main class="spread">
    <section class="back">
      <h2 class="back-title title-metal">Harbor Lanterns</h2>
      <p class="back-subtitle">Hidden Meaning in Your Name</p>

      <div class="method-mark">
        <div class="dot"></div>
        <div class="name">Bright Meadow Method</div>
      </div>

      <p class="blurb">Bright Meadow Method (BMM)® gathers, guides and grounds us in a quiet calling. Grace always meets us where we stand. By learning to listen closely, we are able to gently shape the lives of others, leaving a steady light upon their hearts.</p>

      <div class="promise">
        <p>This book will:</p>
        <ul>
          <li>Reveal the meaning hidden in a name</li>
          <li>Explore the Seven Steady Lanterns</li>
          <li>Chart the Harbor Light Path (HLP)</li>
        </ul>
      </div>

      <p class="bio">International award winning authors, Renata and Walter Oskarsby inspire couples and individuals to find calm and purpose through Bright Meadow Method®. For two decades, they have led gatherings and retreats across the nation and at their quiet lodge set high in the Colorado mountains.</p>

      <blockquote class="verse">“Come, let us go up to the mountain of the LORD, To the house (temple) of the God of Jacob; That He may teach us His ways And that we may walk in His paths.” &nbsp;~Isaiah 2:3</blockquote>

      <div class="contact">
        <p>tallwillowstudio@mailfernly.com</p>
        <p>303.512.4086</p>
        <p class="addr">P.O.Box 718<br>Pinecrest, CO 80417</p>
      </div>
      <div class="isbn-space"></div>
    </section>

    <section class="spine">
      <div class="spine-run">
        <span class="spine-title title-metal">Harbor Lanterns</span>
        <span class="spine-sub">Hidden Meaning<br>in Your Name</span>
        <span class="spine-authors">Walter and Renata<br>Oskarsby</span>
      </div>
    </section>

    <section class="front">
      <h1 class="front-title title-metal">
        <span class="line-one">Harbor</span>
        <span class="line-two">Lanterns</span>
      </h1>
      <p class="front-subtitle">Hidden Meaning<br>in Your Name</p>
      <p class="front-authors">Walter and Renata<br>Oskarsby</p>
    </section>
  </main>
</body>
</html>
```